Sales Flyer for Outdoor Kitchens

Looks to have a trifold flyer designed based off website content / projects. Use www.brickleafyardworks.com for content

```html
<!DOCTYPE html>
<html lang="en">
<head>
<meta charset="UTF-8">
<title>Brickleaf Yardworks – Outdoor Kitchens Trifold</title>
<link rel="stylesheet" href="https://fonts.googleapis.com/css2?family=Montserrat:wght@600;700;800;900&family=Open+Sans:wght@400;600;700&display=swap">
<style>
:root{
  --blue:#1d5fae;
  --blue-dark:#15467f;
  --green:#5bb431;
  --green-dark:#3f8f22;
  --ink:#3a3f45;
  --muted:#6b7178;
  --paper:#ffffff;
  --stage:#eceef1;
  --photo-sky:#b9cfdf;
  --photo-wood:#8a6a4c;
  --photo-stone:#c9bda9;
  --photo-pool:#4aa3c8;
}
*{box-sizing:border-box;margin:0;padding:0}
html,body{width:675px;height:1200px;overflow:hidden}
body{background:var(--stage);font-family:"Open Sans",Arial,sans-serif;color:var(--ink);position:relative}
.spread{position:absolute;left:20px;width:635px;height:490px;background:var(--paper);display:flex;box-shadow:0 2px 8px rgba(0,0,0,.12)}
.spread--outside{top:60px}
.spread--inside{top:640px}
.panel{width:33.333%;height:100%;position:relative;display:flex;flex-direction:column;padding:16px 14px}
.panel + .panel{border-left:1px solid #e3e6ea}
h2,h3,h4{font-family:"Montserrat",Arial,sans-serif}
p{font-size:6.4px;line-height:1.5;color:var(--ink)}
.photo{border-radius:2px}

/* outside: who we are */
.panel--about{background:linear-gradient(160deg,var(--blue) 0%,var(--blue-dark) 100%);color:#fff;padding:28px 18px}
.panel--about h2{font-size:15px;font-weight:800;letter-spacing:.5px;margin-bottom:10px;text-align:center}
.panel--about p{color:#eaf1fa;font-size:7px;text-align:center}
.social{margin-top:auto;display:flex;flex-direction:column;gap:7px}
.social li{list-style:none;display:flex;align-items:center;gap:7px;font-size:6.5px;color:#fff}
.social .dot{width:11px;height:11px;border-radius:50%;background:#fff;opacity:.9}
.green-stripe{position:absolute;left:0;right:0;bottom:0;height:6px;background:var(--green)}

/* outside: contact */
.panel--contact{padding:0}
.panel--contact .photo{height:235px;background:linear-gradient(180deg,var(--photo-sky) 0%,#d9d2c4 45%,var(--photo-wood) 100%);border-radius:0}
.contact-block{background:var(--blue);color:#fff;padding:14px 14px;flex:1;display:flex;flex-direction:column;gap:9px}
.contact-block h3{font-size:13px;font-weight:800}
.contact-row{display:flex;align-items:center;gap:7px;font-size:7px;line-height:1.35}
.contact-row svg{flex:none}
.web-bar{background:var(--green);color:#fff;font-family:"Montserrat",Arial,sans-serif;font-weight:700;font-size:7.5px;text-align:center;padding:9px 4px}

/* outside: cover */
.panel--cover{align-items:center;padding:18px 14px}
.brand{display:flex;align-items:center;gap:6px;margin-bottom:12px}
.brand .mark{width:18px;height:18px;border-radius:50%;background:var(--green)}
.brand span{font-family:"Montserrat",Arial,sans-serif;font-weight:800;font-size:11px;color:var(--blue);letter-spacing:.3px}
.cover-title{text-align:center;font-weight:900;line-height:1.05;margin-bottom:12px}
.cover-title .l1{display:block;font-size:14px;color:var(--blue)}
.cover-title .l2{display:block;font-size:20px;color:var(--green)}
.cover-title .l3{display:block;font-size:14px;color:var(--blue)}
.panel--cover .photo-main{width:100%;height:150px;background:linear-gradient(180deg,var(--photo-sky),var(--photo-stone) 60%,var(--photo-wood))}
.panel--cover .photo-sub{width:100%;height:110px;margin-top:8px;background:linear-gradient(180deg,#9fc3d6,var(--photo-pool) 60%,#2f7fa3)}

/* inside */
.services-title{font-size:15px;font-weight:900;color:var(--blue);line-height:1.05;margin-bottom:7px}
.bar-head{background:var(--green);color:#fff;font-family:"Montserrat",Arial,sans-serif;font-weight:700;font-size:8.5px;padding:4px 7px;margin-bottom:6px}
.item{margin-bottom:6px}
.item h4{font-size:7px;font-weight:700;color:var(--blue);margin-bottom:1px}
.sec-head{font-size:9.5px;font-weight:800;color:var(--green-dark);margin-bottom:3px}
.sec-head.blue{color:var(--blue)}
.panel--inside-mid .photo{height:90px;margin:6px 0;background:linear-gradient(180deg,var(--photo-sky),var(--photo-stone) 55%,var(--photo-wood))}
.panel--inside-mid .photo.fire{background:linear-gradient(180deg,#6a7a86,#a4714a 60%,#d98a3a)}
.panel--inside-right .photo{height:70px;margin:5px 0;background:linear-gradient(180deg,#c5d5e0,#b9a68a 60%,#7c5e42)}
.panel--inside-right .photo.pool{background:linear-gradient(180deg,#a9cbe0,var(--photo-pool) 60%,#2b7498)}
.block{margin-bottom:7px}
.url-bar{margin-top:auto;background:var(--green);color:#fff;font-family:"Montserrat",Arial,sans-serif;font-weight:700;font-size:7.5px;text-align:center;padding:6px 4px}
</style>
</head>
<body>

<!-- Outside spread -->
<section class="spread spread--outside">
  <div class="panel panel--about">
    <h2>WHO WE ARE</h2>
    <p>With over a decade of experience in the industry, our owners and team of craftsmen build outdoor living spaces across the region. We guide every project from first sketch to final walkthrough, so you can relax and enjoy the backyard you always imagined. Our goal is to create stunning and functional spaces for families to gather.</p>
    <ul class="social">
      <li><span class="dot"></span>/brickleafyardworks</li>
      <li><span class="dot"></span>/brickleafyardworks</li>
      <li><span class="dot"></span>/brickleafyardworks</li>
      <li><span class="dot"></span>/brickleafyardworks</li>
    </ul>
    <div class="green-stripe"></div>
  </div>

  <div class="panel panel--contact">
    <div class="photo" role="img" aria-label="Covered outdoor kitchen with stone counter and wooden pavilion"></div>
    <div class="contact-block">
      <h3>Contact</h3>
      <div class="contact-row">
        <svg width="11" height="11" viewBox="0 0 24 24"><path fill="#fff" d="M12 2a7 7 0 0 0-7 7c0 5 7 13 7 13s7-8 7-13a7 7 0 0 0-7-7zm0 9.5A2.5 2.5 0 1 1 12 6.5a2.5 2.5 0 0 1 0 5z"/></svg>
        <span>4820 Cedar Hollow Rd, Suite 120<br>Kingsford, TX 77300</span>
      </div>
      <div class="contact-row">
        <svg width="11" height="11" viewBox="0 0 24 24"><path fill="#fff" d="M6.6 10.8a15 15 0 0 0 6.6 6.6l2.2-2.2c.3-.3.7-.4 1-.2 1.1.4 2.3.6 3.6.6.6 0 1 .4 1 1V20c0 .6-.4 1-1 1C10.6 21 3 13.4 3 4c0-.6.4-1 1-1h3.5c.6 0 1 .4 1 1 0 1.3.2 2.5.6 3.6.1.3 0 .7-.2 1z"/></svg>
        <span>281-555-0147</span>
      </div>
      <div class="contact-row">
        <svg width="11" height="11" viewBox="0 0 24 24"><path fill="#fff" d="M3 5h18v14H3z" opacity=".0"/><path fill="none" stroke="#fff" stroke-width="2" d="M3 6h18v12H3zM3 6l9 7 9-7"/></svg>
        <span>info@brickleafyardworks.com</span>
      </div>
    </div>
    <div class="web-bar">www.brickleafyardworks.com</div>
  </div>

  <div class="panel panel--cover">
    <div class="brand"><span class="mark"></span><span>BRICKLEAF YARDWORKS</span></div>
    <h2 class="cover-title"><span class="l1">Create</span><span class="l2">YOUR DREAM</span><span class="l3">Backyard With Us</span></h2>
    <div class="photo photo-main" role="img" aria-label="Stone outdoor kitchen under a covered patio"></div>
    <div class="photo photo-sub" role="img" aria-label="Backyard pool with pavilion at dusk"></div>
  </div>
</section>

<!-- Inside spread -->
<section class="spread spread--inside">
  <div class="panel panel--inside-left">
    <h2 class="services-title">OUR TURNKEY<br>SERVICES</h2>
    <div class="bar-head">Outdoor Kitchens</div>
    <p class="item">Our team designs and builds custom outdoor kitchens that fit your space, budget and cooking style, from compact grill islands to full entertaining setups.</p>
    <div class="item"><h4>Built-In Grills</h4><p>Premium gas and charcoal grills set into durable stone or brick islands for years of backyard cooking.</p></div>
    <div class="item"><h4>Island Kitchens</h4><p>Counter space, storage and seating in one layout, with finishes chosen to match your home.</p></div>
    <div class="item"><h4>Bar &amp; Seating</h4><p>Raised bars and dining areas that keep guests close to the cook and the conversation.</p></div>
    <div class="item"><h4>Appliances</h4><p>Refrigerators, sinks, burners and pizza ovens installed and connected by our own crew.</p></div>
    <div class="item"><h4>Roofs &amp; Covers</h4><p>Shade structures that protect your kitchen from sun and rain in every season.</p></div>
  </div>

  <div class="panel panel--inside-mid">
    <h3 class="sec-head">Pavilions, Patios &amp; Pergolas</h3>
    <p>We design shaded spaces that extend your living area outdoors, built with quality lumber, stone and metal roofing to stand up to the weather.</p>
    <div class="photo" role="img" aria-label="Wooden pavilion over a stone patio"></div>
    <div class="item"><h4>Outdoor Pavilions</h4><p>Open-air structures with ceiling fans, lighting and room for dining.</p></div>
    <div class="item"><h4>Patios</h4><p>Stamped concrete, pavers and natural stone laid on a solid base.</p></div>
    <h3 class="sec-head">Fire Pits</h3>
    <p>Gather around a custom fire pit built from stone or block, sized for your yard and finished to match your patio.</p>
    <div class="photo fire" role="img" aria-label="Stone fire pit with seating at evening"></div>
  </div>

  <div class="panel panel--inside-right">
    <div class="block">
      <h3 class="sec-head">Fireplaces</h3>
      <p>Outdoor fireplaces bring warmth and a natural focal point to any covered patio.</p>
      <div class="photo" role="img" aria-label="Stone outdoor fireplace under covered patio"></div>
    </div>
    <div class="block">
      <h3 class="sec-head">Pools</h3>
      <p>Custom pools and spas planned together with your patio and kitchen.</p>
      <div class="photo pool" role="img" aria-label="Backyard swimming pool with deck"></div>
    </div>
    <div class="block">
      <h3 class="sec-head">Landscaping &amp; Lighting</h3>
      <p>Plants, stone borders and low-voltage lights that finish the space day and night.</p>
    </div>
    <div class="block">
      <h3 class="sec-head blue">Why Choose Brickleaf Yardworks?</h3>
      <p>One team handles design, permits and construction, with clear pricing and a warranty on our work.</p>
    </div>
    <div class="url-bar">www.brickleafyardworks.com</div>
  </div>
</section>

</body>
</html>
```